Web site for radio show

I've got a radio show starting on VelarOnAir and need a web site for it. I am familiar with WordPress, so I'd like to get a design for a WordPress-based web site for the show.

I'm also posting a logo project to be done at the same time.

The best radio show web site I've seen is the Lantern Tuesday site (www.lanterntuesday.example). That's a good model but I don't want to start with that much complexity and content. The initial site that I'd like you to design would have the following parts:
- Upcoming shows
- Past shows (including links to authors, their web sites, and their books)
- Chirplo feed
- Blog
- About
- ...and anything else you think would be necessary

For colors, I'd like it to be consistent with my personal web site: www.kelbrandthinking.example

Target Market(s)

The target market for this show is mid- to upper-level managers

Industry/Entity Type

Radio

Requirements
Must have
• The project has to proceed in (at least) two stages: a first rough layout, and a second finished design. Whether you want a third stage in between with look and feel options is up to you.

```html
<!DOCTYPE html>
<html lang="en">
<head>
<meta charset="utf-8">
<title>Bright Course Radio Show</title>
<link rel="stylesheet" href="https://fonts.googleapis.com/css2?family=Arimo:wght@400;700&display=swap">
<style>
  :root {
    --nav-bg: #3a3a3a;
    --nav-text: #ffffff;
    --brand-red: #d0202e;
    --headline-gold: #c9860f;
    --muted-grey: #6e6e6e;
    --body-text: #2a2a2a;
    --chirp-blue: #1da1e8;
    --arrow-bg: rgba(200, 200, 200, 0.45);
    --page-bg: #ffffff;
  }
  * { box-sizing: border-box; margin: 0; padding: 0; }
  html, body { width: 1200px; height: 795px; overflow: hidden; background: var(--page-bg); }
  body { font-family: "Arimo", Arial, sans-serif; position: relative; }

  .site-nav {
    position: absolute; top: 0; left: 0; width: 1200px; height: 54px;
    background: var(--nav-bg); z-index: 3;
    display: flex; justify-content: center; align-items: center; gap: 35px;
    padding-right: 20px;
  }
  .site-nav a { color: var(--nav-text); text-decoration: none; font-size: 21px; }

  .host-photo {
    position: absolute; top: 54px; left: 600px; width: 600px; height: 741px;
    background:
      linear-gradient(90deg, #ffffff 0%, rgba(255,255,255,0.55) 14%, rgba(255,255,255,0) 32%),
      radial-gradient(ellipse 45% 40% at 70% 28%, #e9c2b2 0%, #dcb1a2 45%, rgba(220,177,162,0) 75%),
      linear-gradient(180deg, #f1ecea 0%, #ede6e4 50%, #b8b2b0 75%, #8f8b8c 100%);
  }

  .brand { position: absolute; left: 32px; top: 112px; display: flex; align-items: center; gap: 18px; }
  .brand-dot { width: 46px; height: 46px; border-radius: 50%; background: var(--brand-red); }
  .brand-name { font-size: 64px; font-weight: 400; color: var(--brand-red); letter-spacing: 1px; }
  .brand-tagline {
    position: absolute; left: 67px; top: 241px; font-size: 19px; line-height: 23px; color: var(--muted-grey);
  }

  .hero-headline {
    position: absolute; left: 155px; top: 350px; font-size: 40px; line-height: 47px;
    font-weight: 400; color: var(--headline-gold);
  }
  .hero-intro {
    position: absolute; left: 171px; top: 445px; width: 340px;
    font-size: 14.5px; line-height: 18px; color: var(--body-text);
  }

  .slider-arrow {
    position: absolute; top: 378px; width: 64px; height: 64px; border-radius: 50%;
    background: var(--arrow-bg); display: flex; align-items: center; justify-content: center; z-index: 2;
  }
  .slider-arrow.prev { left: 7px; }
  .slider-arrow.next { left: 1127px; opacity: 0.45; }

  .quick-links {
    position: absolute; left: 50px; top: 596px; display: flex; gap: 18px; list-style: none;
  }
  .quick-link { width: 114px; text-align: center; }
  .quick-link a { text-decoration: none; color: var(--body-text); font-size: 19px; line-height: 22px; }
  .quick-icon {
    width: 112px; height: 112px; border-radius: 50%; margin: 0 auto 13px;
    display: flex; align-items: center; justify-content: center;
  }
  .icon-solid { background: var(--brand-red); border: 3px solid #f2c6c9; }
  .icon-outline { border: 3px solid var(--brand-red); background: #fff; }
  .icon-chirp { background: var(--chirp-blue); border: 3px solid #cfeaf8; }
  .blog-word { font-size: 33px; font-weight: 700; color: var(--brand-red); letter-spacing: 1px; }
</style>
</head>
<body>
  <nav class="site-nav">
    <a href="#">About</a>
    <a href="#">Upcoming Shows</a>
    <a href="#">Past Shows</a>
    <a href="#">Blog</a>
    <a href="#">Chirplo Feed</a>
    <a href="#">Contact</a>
  </nav>

  <div class="host-photo" role="img" aria-label="Portrait of the show host in glasses and a checked jacket, fading into white on the left"></div>

  <header class="brand">
    <span class="brand-dot"></span>
    <span class="brand-name">BRIGHT COURSE</span>
  </header>
  <p class="brand-tagline">Radio Show with Martin Kelbrand<br>on VelarOnAir</p>

  <a class="slider-arrow prev" href="#" aria-label="Previous slide">
    <svg width="22" height="36" viewBox="0 0 22 36"><polyline points="18,3 4,18 18,33" fill="none" stroke="#fff" stroke-width="2.5"/></svg>
  </a>
  <a class="slider-arrow next" href="#" aria-label="Next slide">
    <svg width="22" height="36" viewBox="0 0 22 36"><polyline points="4,3 18,18 4,33" fill="none" stroke="#fff" stroke-width="2.5"/></svg>
  </a>

  <h1 class="hero-headline">HELPING COMPANIES<br>BOOST INNOVATION</h1>
  <p class="hero-intro">Welcome to Bright Course Radio Show. Find dates for upcoming shows. Listen to past shows and get updates through the blog and Chirplo.</p>

  <ul class="quick-links">
    <li class="quick-link">
      <a href="#">
        <div class="quick-icon icon-solid">
          <svg width="60" height="72" viewBox="0 0 60 72" fill="none" stroke="#fff" stroke-width="3">
            <circle cx="30" cy="10" r="4" fill="#fff"/>
            <path d="M30 14 L14 68 M30 14 L46 68 M22 40 H38 M18 54 H42 M25 28 H35"/>
            <path d="M8 4 Q2 12 8 20 M52 4 Q58 12 52 20"/>
          </svg>
        </div>
        Upcoming<br>Shows
      </a>
    </li>
    <li class="quick-link">
      <a href="#">
        <div class="quick-icon icon-outline">
          <svg width="78" height="60" viewBox="0 0 78 60">
            <line x1="20" y1="14" x2="62" y2="2" stroke="#d0202e" stroke-width="3"/>
            <rect x="4" y="14" width="70" height="44" rx="6" fill="#d0202e"/>
            <rect x="12" y="22" width="54" height="10" fill="#fff"/>
            <circle cx="56" cy="45" r="7" fill="#fff"/>
            <g stroke="#fff" stroke-width="2.5"><line x1="14" y1="38" x2="14" y2="52"/><line x1="20" y1="38" x2="20" y2="52"/><line x1="26" y1="38" x2="26" y2="52"/><line x1="32" y1="38" x2="32" y2="52"/><line x1="38" y1="38" x2="38" y2="52"/></g>
          </svg>
        </div>
        Past Shows
      </a>
    </li>
    <li class="quick-link">
      <a href="#">
        <div class="quick-icon icon-outline"><span class="blog-word">BLOG</span></div>
        Blog
      </a>
    </li>
    <li class="quick-link">
      <a href="#">
        <div class="quick-icon icon-chirp"></div>
        Chirplo Feed
      </a>
    </li>
  </ul>
</body>
</html>
```